Business card design for a dynamic IT consulting company

We need a business card design for a young firm, specialized in the Telecommunications/Consulting industry. The name of the company is Brask and Partners Business Consulting Ltd. (Short name: Brask and Partnes)
Brask = solve read reverse, so we aim to be uncomplicated and solution-oriented. The small pipe in our logo is also related to the word solve. So we need a new business card design, which is simple, eye catching and something non traditional (I would probably prefer a square shaped design rather than a rectangle, but open for suggestions). Attached our logo.

Target Market(s)

Usually our customers are Tier1 Telecoms providers (Q-Linkra, Parnexo, etc) and their executives.

Industry/Entity Type

Business

Contact Information for Business Card

Name: Gergely Halmindo
Email: g.halmindo@braskpartnera.hu
Web: www.braskpartnera.hu
Mobile: +36 30 555 0192
Title: Managing Director

Optional:
Company name: Brask and Partners Ltd.
Address: 1047 Budapest, Ravaszi str. 17/B, Hungary

Font styles to use
Other font styles liked:
• helveticaneue_medium, Prime Regular are used now.

Colors

Designer to choose colors to be used in the design.

Requirements
Must have
• I would like to have a 2 sided design.
Nice to have
• I thought if we make the logo a bit bigger (without the company name), that could go to the back with the company name below. I though, if the pipe in the logo is somehow touchable on the business card, would be nice and unique.

```html
<!DOCTYPE html>
<html lang="en">
<head>
<meta charset="utf-8">
<title>Brask and Partners – Business Card</title>
<link rel="stylesheet" href="https://fonts.googleapis.com/css2?family=Open+Sans:wght@400;600;700&display=swap">
<style>
  :root {
    --page-bg: #ecebe8;
    --card-white: #ffffff;
    --brand-blue: #1497d6;
    --brand-grey: #555658;
    --brand-magenta: #b2399a;
    --icon-tab: #4a4b4d;
    --text-light: #ffffff;
    --card-shadow: rgba(0, 0, 0, 0.16);
  }
  html, body {
    margin: 0;
    padding: 0;
    width: 1200px;
    height: 1200px;
    overflow: hidden;
    background: var(--page-bg);
  }
  .canvas {
    width: 1200px;
    height: 1200px;
    display: flex;
    flex-direction: column;
    align-items: center;
    justify-content: center;
    gap: 70px;
  }
  .card {
    width: 880px;
    height: 503px;
    display: block;
    box-shadow: 0 6px 22px var(--card-shadow);
    background: var(--card-white);
  }
  .wordmark {
    font-family: "Open Sans", sans-serif;
    font-weight: 400;
    fill: var(--brand-grey);
  }
  .wordmark-square { fill: var(--brand-blue); }
  .accent-magenta { fill: var(--brand-magenta); }
  .accent-grey { fill: var(--brand-grey); }
  .accent-blue { fill: var(--brand-blue); }
  .back-panel { fill: var(--brand-blue); }
  .icon-tab { fill: var(--icon-tab); }
  .icon { fill: var(--text-light); }
  .icon-stroke { fill: none; stroke: var(--text-light); stroke-width: 1.4; }
  .holder-name {
    font-family: "Open Sans", sans-serif;
    font-weight: 700;
    font-size: 25px;
    fill: var(--text-light);
  }
  .holder-title {
    font-family: "Open Sans", sans-serif;
    font-weight: 600;
    font-size: 16px;
    fill: var(--text-light);
  }
  .contact-line {
    font-family: "Open Sans", sans-serif;
    font-weight: 400;
    font-size: 11.5px;
    fill: var(--text-light);
  }
</style>
</head>
<body>
<main class="canvas">

  <!-- Front of card -->
  <svg class="card card-front" viewBox="0 0 560 320" aria-label="Business card front">
    <rect width="560" height="320" fill="var(--card-white)"/>
    <g class="front-logo">
      <rect class="wordmark-square" x="165" y="132" width="22" height="22"/>
      <text class="wordmark" x="198" y="152" font-size="30">Brask &amp; Partners</text>
    </g>
    <g class="front-stripe">
      <rect class="accent-magenta" x="30" y="266" width="190" height="7"/>
      <rect class="accent-grey" x="220" y="266" width="80" height="7"/>
      <rect class="accent-blue" x="300" y="266" width="230" height="7"/>
    </g>
  </svg>

  <!-- Back of card -->
  <svg class="card card-back" viewBox="0 0 560 320" aria-label="Business card back">
    <rect width="560" height="320" fill="var(--card-white)"/>
    <polygon class="back-panel" points="270,0 560,0 560,230 318,230 318,118 290,96 270,96"/>

    <g class="back-logo">
      <rect class="wordmark-square" x="42" y="152" width="14" height="14"/>
      <text class="wordmark" x="64" y="167" font-size="21">Brask &amp; Partners</text>
    </g>

    <text class="holder-name" x="332" y="66">Gergely Halmindo</text>
    <text class="holder-title" x="332" y="88">Managing Director</text>

    <polygon class="icon-tab" points="300,120 332,120 332,240 316,252 300,240"/>

    <g class="contact-icons">
      <path class="icon" d="M316 129 a5 5 0 0 1 5 5 c0 4 -5 9 -5 9 s-5 -5 -5 -9 a5 5 0 0 1 5 -5z"/>
      <circle cx="316" cy="134" r="1.8" fill="var(--icon-tab)"/>
      <path class="icon" d="M311 160 l3 -2 2 3.5 -1.8 1.2 c1 2 2.5 3.5 4.5 4.5 l1.2 -1.8 3.5 2 -2 3 c-5 -0.5 -10 -5.5 -10.4 -10.4z"/>
      <rect class="icon-stroke" x="309.5" y="187" width="13" height="9"/>
      <path class="icon-stroke" d="M309.5 187 l6.5 5 6.5 -5"/>
      <circle class="icon-stroke" cx="316" cy="219" r="6"/>
      <path class="icon-stroke" d="M310 219 h12 M316 213 c-3 3 -3 9 0 12 c3 -3 3 -9 0 -12"/>
    </g>

    <g class="contact-details">
      <text class="contact-line" x="344" y="132">1047 Budapest, Ravaszi str.</text>
      <text class="contact-line" x="344" y="147">17/B, Hungary</text>
      <text class="contact-line" x="344" y="168">+36 30 555 0192</text>
      <text class="contact-line" x="344" y="195">g.halmindo@braskpartnera.hu</text>
      <text class="contact-line" x="344" y="223">www.braskpartnera.hu</text>
    </g>
  </svg>

</main>
</body>
</html>
```